Logo for a Food & Beverage Franchise Company

We need a logo and stationary for a new company that just aquired a restaurant franchise. We need a sleep and professional logo with stationary.

Target Market(s)

Adults, resturaunt owners, franchisors (Companies who own food franchise companies such as Parvelli Head Office, Tollwick Grill International Franchise)
and Big Food and Beverage who wish to give franchise rights to us)

Industry/Entity Type

Restaurant

Logo Text

Velvet Harbor

Logo styles of interest
Emblem Logo
Pictorial/Combination Logo
Character Logo
Font styles to use
Serif
Sans Serif

Colors
ffc214
f78f20
f37022
faa54b
fece3e
fbed22

Requirements
Must have
• Maximum three color. The less the better.
Nice to have
• It does not have to have a crown, but if you wish to have a crown then it does not have to be so sharp and clear. Abstract is better.

```html
<!DOCTYPE html>
<html lang="en">
<head>
<meta charset="utf-8">
<title>Velvet Harbor — Stationery Set</title>
<link rel="stylesheet" href="https://fonts.googleapis.com/css2?family=Montserrat:wght@400;500;600&display=swap">
<style>
  :root {
    --backdrop: #4a4a4a;
    --ink-black: #1e1e1e;
    --paper: #ffffff;
    --gold: #c9a43a;
    --hub-grey: #5a5a5a;
    --text-dark: #222222;
    --shadow: rgba(0, 0, 0, 0.35);
  }
  html, body {
    margin: 0;
    width: 1200px;
    height: 900px;
    overflow: hidden;
    background: var(--backdrop);
    font-family: "Montserrat", sans-serif;
  }
  .canvas { position: relative; width: 1200px; height: 900px; }
  .sheet { position: absolute; box-shadow: 0 6px 18px var(--shadow); box-sizing: border-box; }

  .wordmark {
    font-family: "Montserrat", sans-serif;
    font-weight: 500;
    text-transform: uppercase;
    letter-spacing: 0.3em;
    white-space: nowrap;
    display: flex;
    align-items: center;
    gap: 0.6em;
  }
  .wordmark--gold { color: var(--gold); }
  .wordmark--dark { color: var(--text-dark); }
  .wordmark__dot { width: 0.8em; height: 0.8em; background: currentColor; }

  /* Presentation folder */
  .folder { left: 380px; top: 40px; width: 300px; height: 420px; background: var(--ink-black); }
  .folder .wordmark--small { position: absolute; top: 18px; right: 18px; font-size: 7px; }
  .folder .wordmark--hero { position: absolute; top: 200px; left: 0; right: 0; justify-content: center; font-size: 17px; }

  /* Letterhead */
  .letterhead { left: 720px; top: 40px; width: 300px; height: 424px; background: var(--paper); padding: 22px 24px; color: var(--text-dark); }
  .letterhead__head { display: flex; flex-direction: column; align-items: flex-end; gap: 6px; }
  .letterhead__head .wordmark { font-size: 8px; }
  .letterhead__address { font-size: 5.5px; line-height: 1.5; text-align: right; }
  .letterhead__body { margin-top: 26px; font-size: 6.5px; line-height: 1.6; }
  .letterhead__body p { margin: 0 0 8px; }
  .letterhead__foot { position: absolute; left: 24px; bottom: 20px; font-size: 6px; }

  /* Business cards */
  .card { width: 120px; height: 170px; background: var(--ink-black); }
  .card--front { left: 210px; top: 250px; }
  .card--front .wordmark { position: absolute; top: 78px; left: 0; right: 0; justify-content: center; font-size: 8px; }
  .card--back { left: 70px; top: 250px; padding: 16px 12px; color: var(--paper); }
  .card--back .wordmark { font-size: 6px; margin-bottom: 52px; }
  .card__name { font-size: 7px; font-weight: 600; color: var(--gold); }
  .card__role { font-size: 5.5px; margin: 2px 0 10px; }
  .card__contact { font-size: 5.5px; line-height: 1.6; }

  /* Disc */
  .disc { left: 70px; top: 490px; width: 220px; height: 220px; border-radius: 50%; background: var(--ink-black); }
  .disc__hub { position: absolute; left: 80px; top: 80px; width: 60px; height: 60px; border-radius: 50%; background: var(--hub-grey); }
  .disc__hole { position: absolute; left: 100px; top: 100px; width: 20px; height: 20px; border-radius: 50%; background: var(--backdrop); }
  .disc .wordmark { position: absolute; top: 44px; left: 0; right: 0; justify-content: center; font-size: 7px; }

  /* Envelope */
  .envelope { left: 380px; top: 510px; width: 620px; height: 300px; background: var(--paper); }
  .envelope__band { position: absolute; left: 0; right: 0; top: 100px; height: 64px; background: var(--ink-black); display: flex; align-items: center; justify-content: center; }
  .envelope__band .wordmark { font-size: 15px; }
  .envelope .wordmark--corner { position: absolute; top: 20px; left: 22px; font-size: 7px; }
  .envelope__contact { position: absolute; right: 24px; bottom: 20px; font-size: 8px; line-height: 1.55; color: var(--text-dark); text-align: right; }
</style>
</head>
<body>
<main class="canvas">

  <section class="sheet folder" aria-label="Presentation folder">
    <div class="wordmark wordmark--gold wordmark--small"><span class="wordmark__dot"></span>Velvet Harbor</div>
    <div class="wordmark wordmark--gold wordmark--hero">Velvet Harbor</div>
  </section>

  <section class="sheet letterhead" aria-label="Letterhead">
    <header class="letterhead__head">
      <div class="wordmark wordmark--dark"><span class="wordmark__dot"></span>Velvet Harbor</div>
      <div class="letterhead__address">
        P.O. Box 40217, Dubai, UAE<br>
        +974 300 4100<br>
        info@velvetharbor.com
      </div>
    </header>
    <div class="letterhead__body">
      <p>Dear partner, thank you for your continued interest in our franchise group. We are pleased to share the next steps for the new season and the timeline we agreed.</p>
      <p>Our team will visit each site during the first month to review kitchen layout, staff training and supply routes. Please prepare the floor plans and current menus before our arrival.</p>
      <p>We look forward to a long and rewarding partnership with you and your guests.</p>
      <p>Kind regards,<br>Management Office</p>
    </div>
    <div class="letterhead__foot wordmark wordmark--dark">Velvet Harbor</div>
  </section>

  <section class="sheet card card--back" aria-label="Business card, contact side">
    <div class="wordmark wordmark--gold">Velvet Harbor</div>
    <div class="card__name">Samir Haddad</div>
    <div class="card__role">Franchise Director</div>
    <div class="card__contact">+974 300 4100<br>info@velvetharbor.com</div>
  </section>

  <section class="sheet card card--front" aria-label="Business card, brand side">
    <div class="wordmark wordmark--gold">Velvet Harbor</div>
  </section>

  <section class="sheet disc" aria-label="Disc label">
    <div class="wordmark wordmark--gold">Velvet Harbor</div>
    <div class="disc__hub"></div>
    <div class="disc__hole"></div>
  </section>

  <section class="sheet envelope" aria-label="Envelope">
    <div class="wordmark wordmark--dark wordmark--corner"><span class="wordmark__dot"></span>Velvet Harbor</div>
    <div class="envelope__band">
      <div class="wordmark wordmark--gold">Velvet Harbor</div>
    </div>
    <address class="envelope__contact">
      Office: +974 300 4100<br>
      Mobile: +971 50 600 2718<br>
      Email: info@velvetharbor.com<br>
      P.O. Box 40217, Dubai, UAE<br>
      www.velvetharbor.com
    </address>
  </section>

</main>
</body>
</html>
```